Website Design for a holiday home letting busines

We require a redesign of our present website www.birchwoodstays.com. We want the website to stand out and look professional and clean to make holiday hunters want to book a caravan or lodge holiday with us. Our logo is red however we DO NOT want the website to be red. We want a natural colour scheme.

The final design should communicate that we are a professional company to book with.

On the home page we require;
Overview of company
Photo
Search box for holiday (check in)
Late Deals
Reviews
News

We would like the following pages designed; home page, available dates page, caravans page, content page.

The website should be responsive for smart phones. One website I do like is http://www.verdamoro.be/nl/

Target Market(s)

Families

Industry/Entity Type

Travel

Number of Pages Required

5+ page

Font styles to use
Serif

Requirements
Must have
• The project must be responsive for mobile phones and tablets.
• Ability to search for holiday home holidays
• We want a natural colour scheme.
Nice to have
• A style we like is http://www.verdamoro.be/nl/
Should not have
• Do not use red as a colour for the website. Our logo is red so this is the only time we want this used.

```html
<!DOCTYPE html>
<html lang="en">
<head>
<meta charset="utf-8">
<title>Birchwood Stays – Holiday Homes</title>
<link rel="stylesheet" href="https://fonts.googleapis.com/css2?family=Oswald:wght@400;600&family=Roboto+Slab:wght@400;700&family=Open+Sans:wght@400;600;700&display=swap">
<style>
:root{
  --page:#f4f4f2;
  --ink:#3a3a3a;
  --muted:#8a8a8a;
  --line:#dcdcdc;
  --accent:#1f6fb5;
  --accent-dark:#17578f;
  --header:#262626;
  --nav:#1e1e1e;
  --footer:#1b1b1b;
  --footer-text:#bdbdbd;
  --white:#ffffff;
  --shade:rgba(8,8,10,.74);
  --modal:#121212;
}
*{box-sizing:border-box;margin:0;padding:0}
html,body{width:1200px;height:2884px;overflow:hidden}
body{position:relative;background:var(--page);font-family:"Open Sans",Arial,sans-serif;color:var(--ink);font-size:13px}
.abs{position:absolute}

/* header */
.site-header{left:0;top:0;width:1200px;height:124px;background:var(--header)}
.brand{left:230px;top:28px;display:flex;align-items:center;gap:14px;color:var(--white);font-family:"Open Sans",sans-serif;font-weight:700;font-size:26px}
.brand-dot{width:46px;height:46px;border-radius:50%;background:#b8322f}
.contact{top:40px;display:flex;align-items:center;gap:10px;color:#d0d0d0;font-size:15px}
.contact .ic{width:28px;height:28px;border-radius:50%;border:2px solid #d0d0d0}
.main-nav{left:0;top:124px;width:1200px;height:56px;background:var(--nav);display:flex;justify-content:center;align-items:center;gap:30px}
.main-nav a{color:#e6e6e6;text-decoration:none;font-size:13px;font-weight:600;text-transform:uppercase;letter-spacing:.5px}

/* hero */
.hero{left:0;top:180px;width:1200px;height:480px;background:linear-gradient(120deg,#4a3a2a 0%,#7a6248 40%,#a48b68 70%,#5d4c3a 100%)}
.hero-title{left:72px;top:260px;font-family:"Oswald",sans-serif;font-weight:600;font-size:60px;color:var(--white);letter-spacing:1px}
.hero-text{left:72px;top:352px;width:520px;color:#eee;font-size:15px;line-height:22px}
.hero-btn{left:72px;top:440px;padding:8px 20px;border:2px solid var(--white);color:var(--white);font-size:13px;text-transform:uppercase}

/* search */
.search-box{left:100px;top:600px;width:1000px;height:120px;background:var(--white);box-shadow:0 2px 6px rgba(0,0,0,.15);display:flex;align-items:center;padding:0 40px;gap:20px}
.search-box .field{flex:1;height:44px;border:1px solid var(--line);padding:12px;color:var(--muted)}
.search-box .go{width:150px;height:44px;background:var(--accent);color:var(--white);display:flex;align-items:center;justify-content:center;font-weight:700;text-transform:uppercase}

/* sections */
.section-title{font-family:"Roboto Slab",serif;font-weight:700;font-size:20px;color:var(--accent);text-transform:uppercase;letter-spacing:2px}
.overview-title{left:100px;top:768px}
.overview-text{left:100px;top:812px;width:620px;line-height:22px;color:#555}
.overview-text p{margin-bottom:14px}
.video{left:740px;top:800px;width:360px;height:200px;background:linear-gradient(135deg,#6f8aa6,#9fb6c8 50%,#5c7288)}
.video-bar{left:740px;top:972px;width:360px;height:28px;background:rgba(0,0,0,.55)}
.arrows{display:flex;gap:6px}
.arrows span{width:26px;height:26px;background:#cfcfcf;display:block}

.card{width:310px;height:400px;background:var(--white);border:1px solid var(--line)}
.card .photo{height:150px;background:linear-gradient(135deg,#8a6a4a,#c9a57c 55%,#6f553d)}
.card .body{padding:14px 16px}
.card .type{font-size:12px;color:var(--muted)}
.card .name{font-size:14px;font-weight:700;color:var(--accent);margin:4px 0 8px}
.card .meta{display:flex;justify-content:space-between;font-size:12px;color:#666;border-top:1px solid var(--line);border-bottom:1px solid var(--line);padding:8px 0;margin-bottom:10px}
.card .feat{display:flex;gap:10px;align-items:center;font-size:12px;color:#666;margin-bottom:8px}
.card .feat i{width:18px;height:14px;background:var(--accent);display:block}
.card .book{margin:14px auto 0;width:150px;height:34px;background:var(--accent);color:var(--white);font-size:12px;font-weight:700;display:flex;align-items:center;justify-content:center;text-transform:uppercase}

/* columns */
.col{width:310px}
.col-head{height:40px;background:var(--accent);color:var(--white);font-family:"Roboto Slab",serif;font-weight:700;font-size:16px;letter-spacing:1.5px;padding:10px 14px;text-transform:uppercase}
.item{display:flex;gap:12px;padding:14px 0;border-bottom:1px solid var(--line)}
.item .thumb{width:90px;height:74px;flex:none;background:linear-gradient(135deg,#7f9a86,#b6c7a8)}
.item h4{font-size:13px;color:var(--accent);margin-bottom:4px}
.item p{font-size:12px;line-height:17px;color:#666}
.item .date{font-size:11px;color:var(--muted);margin-top:4px}

/* footer */
.site-footer{left:0;top:2592px;width:1200px;height:292px;background:var(--footer)}
.f-col{top:2620px;color:var(--footer-text)}
.f-col h5{font-size:13px;color:var(--white);text-transform:uppercase;margin-bottom:14px;letter-spacing:1px}
.f-col li{list-style:none;font-size:13px;margin-bottom:9px;display:flex;align-items:center;gap:10px}
.f-col li::before{content:"";width:8px;height:8px;background:var(--white);display:block}
.f-input{width:240px;height:36px;background:#2c2c2c;margin-bottom:10px}
.f-btn{width:110px;height:32px;background:var(--accent);color:var(--white);font-size:11px;font-weight:700;display:flex;align-items:center;justify-content:center}
.copy{left:80px;top:2836px;color:#777;font-size:12px}
.social{left:1000px;top:2818px;display:flex;gap:8px}
.social span{width:32px;height:32px;border-radius:50%;border:2px solid #999;display:block}

/* overlay + login */
.shade{left:0;top:0;width:1200px;height:2884px;background:var(--shade)}
.login{left:288px;top:520px;width:600px;height:368px;background:var(--modal);border:14px solid var(--white);text-align:center}
.login h2{margin-top:56px;font-size:20px;font-weight:600;color:var(--white);letter-spacing:1px}
.login .input{margin:12px auto 0;width:480px;height:46px;background:var(--white);text-align:left;padding:14px 12px;font-size:13px;color:#333;font-weight:600}
.login .input:first-of-type{margin-top:28px}
.login .actions{width:480px;margin:22px auto 0;display:flex;align-items:center;gap:20px}
.login .signin{width:104px;height:38px;background:var(--accent);color:var(--white);font-weight:700;font-size:14px;display:flex;align-items:center;justify-content:center}
.login .register{color:var(--white);font-weight:600;font-size:14px;text-decoration:underline}
.close{left:858px;top:504px;width:44px;height:44px;border-radius:50%;background:var(--accent);border:3px solid var(--white)}
</style>
</head>
<body>

<header class="abs site-header">
  <div class="abs brand"><span class="brand-dot"></span>Birchwood Stays</div>
  <div class="abs contact" style="left:660px"><span class="ic"></span>01632 960 214</div>
  <div class="abs contact" style="left:860px"><span class="ic"></span>hello@birchwoodstays.com</div>
</header>
<nav class="abs main-nav">
  <a>Home</a><a>Lodges</a><a>Caravan Holidays</a><a>Late Deals</a><a>Available Dates</a><a>Property Owners</a><a>Reviews</a><a>News</a><a>Contact</a>
</nav>

<section class="abs hero" role="img" aria-label="Photo of a cosy holiday lodge interior"></section>
<h1 class="abs hero-title">NO DEPOSIT HOLIDAYS</h1>
<p class="abs hero-text">Book your lodge or caravan break today with no deposit to pay up front.</p>
<div class="abs hero-btn">Read More</div>

<div class="abs search-box">
  <div class="field">Check in date</div>
  <div class="field">Nights</div>
  <div class="field">Park</div>
  <div class="go">Search</div>
</div>

<h2 class="abs section-title overview-title">Overview of Company</h2>
<div class="abs overview-text">
  <p>Birchwood Stays offers quality holiday lodges and caravans across beautiful country parks, perfect for families looking to relax and explore.</p>
  <p>Every home is checked by our team before you arrive, with fresh linen, full kitchens and plenty of space for the whole family.</p>
  <p>Booking is simple and secure, and our friendly staff are here to help every step of the way.</p>
</div>
<div class="abs video" role="img" aria-label="Video still of a holiday park"></div>
<div class="abs video-bar"></div>

<h2 class="abs section-title" style="left:100px;top:1060px">Late Deals</h2>
<div class="abs arrows" style="left:1046px;top:1060px"><span></span><span></span></div>

<article class="abs card" style="left:100px;top:1124px">
  <div class="photo" role="img" aria-label="Photo of a lodge bedroom"></div>
  <div class="body">
    <div class="type">Caravan Lodge</div><div class="name">Oak View Lodge, Lakeside Park</div>
    <div class="meta"><span>3 nights from</span><span>£249</span></div>
    <div class="feat"><i></i>Sleeps 6</div><div class="feat"><i></i>3 Bedrooms</div>
    <div class="book">Book Now</div>
  </div>
</article>
<article class="abs card" style="left:445px;top:1124px">
  <div class="photo" role="img" aria-label="Photo of a caravan lounge"></div>
  <div class="body">
    <div class="type">Static Caravan</div><div class="name">Willow Caravan, Meadow Park</div>
    <div class="meta"><span>4 nights from</span><span>£199</span></div>
    <div class="feat"><i></i>Sleeps 4</div><div class="feat"><i></i>2 Bedrooms</div>
    <div class="book">Book Now</div>
  </div>
</article>
<article class="abs card" style="left:790px;top:1124px">
  <div class="photo" role="img" aria-label="Photo of a lodge living room"></div>
  <div class="body">
    <div class="type">Luxury Lodge</div><div class="name">Pine Retreat, Forest Edge</div>
    <div class="meta"><span>7 nights from</span><span>£499</span></div>
    <div class="feat"><i></i>Sleeps 8</div><div class="feat"><i></i>4 Bedrooms</div>
    <div class="book">Book Now</div>
  </div>
</article>

<h2 class="abs section-title" style="left:100px;top:1590px">List of Caravans and Lodges</h2>
<div class="abs arrows" style="left:1046px;top:1590px"><span></span><span></span></div>

<article class="abs card" style="left:100px;top:1656px">
  <div class="photo" role="img" aria-label="Photo of a caravan bedroom"></div>
  <div class="body">
    <div class="type">Static Caravan</div><div class="name">Heather Caravan, Hillside Park</div>
    <div class="meta"><span>Per week from</span><span>£399</span></div>
    <div class="feat"><i></i>Sleeps 6</div><div class="feat"><i></i>3 Bedrooms</div>
    <div class="book">Details</div>
  </div>
</article>
<article class="abs card" style="left:445px;top:1656px">
  <div class="photo" role="img" aria-label="Photo of a lodge bedroom"></div>
  <div class="body">
    <div class="type">Holiday Lodge</div><div class="name">Birch Lodge, Riverside Park</div>
    <div class="meta"><span>Per week from</span><span>£549</span></div>
    <div class="feat"><i></i>Sleeps 4</div><div class="feat"><i></i>2 Bedrooms</div>
    <div class="book">Details</div>
  </div>
</article>
<article class="abs card" style="left:790px;top:1656px">
  <div class="photo" role="img" aria-label="Photo of a lodge interior"></div>
  <div class="body">
    <div class="type">Luxury Lodge</div><div class="name">Elm Lodge, Valley Park</div>
    <div class="meta"><span>Per week from</span><span>£649</span></div>
    <div class="feat"><i></i>Sleeps 6</div><div class="feat"><i></i>3 Bedrooms</div>
    <div class="book">Details</div>
  </div>
</article>

<section class="abs col" style="left:100px;top:2110px">
  <div class="col-head">Latest Reviews</div>
  <div class="item"><div><h4>“Lovely family break”</h4><p>Spotless lodge, great park and very helpful staff. We will be back next summer.</p><div class="date">Sarah, June 2014</div></div></div>
  <div class="item"><div><h4>“Perfect for the kids”</h4><p>Plenty to do on site and the caravan had everything we needed for the week.</p><div class="date">Mark, May 2014</div></div></div>
  <div class="item"><div><h4>“Easy to book”</h4><p>Simple booking, no deposit and a warm welcome when we arrived.</p><div class="date">Helen, May 2014</div></div></div>
</section>
<section class="abs col" style="left:445px;top:2110px">
  <div class="col-head">Latest Blogs</div>
  <div class="item"><div class="thumb" role="img" aria-label="Blog photo of a lakeside walk"></div><div><h4>Summer walks nearby</h4><p>Our favourite family trails close to the parks.</p><div class="date">12 June 2014</div></div></div>
  <div class="item"><div class="thumb" role="img" aria-label="Blog photo of a new lodge"></div><div><h4>New lodges added</h4><p>Three new luxury lodges now open to book.</p><div class="date">2 June 2014</div></div></div>
  <div class="item"><div class="thumb" role="img" aria-label="Blog photo of a park event"></div><div><h4>Half term events</h4><p>Fun activities planned for the whole family.</p><div class="date">20 May 2014</div></div></div>
</section>
<section class="abs col" style="left:790px;top:2110px">
  <div class="col-head">Community Feed</div>
  <div class="item"><div class="thumb" role="img" aria-label="Guest holiday photo"></div><div><h4>Birchwood Stays</h4><p>Last minute lodge free this weekend, call us now.</p><div class="date">2 hours ago</div></div></div>
  <div class="item"><div class="thumb" role="img" aria-label="Guest holiday photo"></div><div><h4>Birchwood Stays</h4><p>Thanks to all our guests for lovely reviews.</p><div class="date">1 day ago</div></div></div>
  <div class="item"><div class="thumb" role="img" aria-label="Guest holiday photo"></div><div><h4>Birchwood Stays</h4><p>Autumn dates now open for booking online.</p><div class="date">3 days ago</div></div></div>
</section>

<footer class="abs site-footer"></footer>
<div class="abs f-col" style="left:80px"><h5>About Us</h5><ul><li>Home</li><li>Our Parks</li><li>Late Deals</li><li>Reviews</li><li>Contact</li></ul></div>
<div class="abs f-col" style="left:330px"><h5>Holiday Info</h5><ul><li>Lodges</li><li>Caravans</li><li>Available Dates</li><li>FAQs</li><li>Terms</li></ul></div>
<div class="abs f-col" style="left:590px"><h5>Property Owners</h5><ul><li>List Your Home</li><li>Our Fees</li><li>Owner Login</li></ul></div>
<div class="abs f-col" style="left:860px"><h5>Newsletter</h5><div class="f-input"></div><div class="f-btn">SUBSCRIBE</div></div>
<div class="abs copy">© 2014 Birchwood Stays</div>
<div class="abs social"><span></span><span></span><span></span></div>

<div class="abs shade"></div>
<div class="abs login">
  <h2>LOGIN</h2>
  <div class="input">EMAIL</div>
  <div class="input">PASSWORD</div>
  <div class="actions"><div class="signin">SIGN IN</div><span class="register">REGISTERED HERE</span></div>
</div>
<div class="abs close">
  <svg width="38" height="38" viewBox="0 0 38 38"><path d="M13 13l12 12M25 13L13 25" stroke="#fff" stroke-width="3" stroke-linecap="round"/></svg>
</div>

</body>
</html>
```